Business Card Design for new consultancy company

Name of Company: Orbit Lanternway
Nature of Business: Digital Business Consultancy
Specialises in Digital Media Strategy, Digital Business Model Transformation, Over-The-Top (OTT) Development, Web Business Development, Digital Marketing, Web and App Product Development, Design and Innovation

Website: http://www.orbit-lanternway.example

Designs can be of any colour or any number of colours, objective is to give the impression we are a digital trend setter, creative and impactful.

Also please suggest a logo to complement the name and business card.

Target Market(s)

Media Companies, Telcos, Enterprises

Industry/Entity Type

Business

Contact Information for Business Card

Standard business card size. OK with to play with small variations like corners for impact/impression.

Font styles to use
Serif
Sans Serif

Requirements
Must have
• Clarity, Impact, Creativity
Nice to have
• Design should encapsulate professionalism, expertise, yet trend-setting and vibrant for digital consultancy
Should not have
• Messy layout, too gaudy colours or design

```html
<!DOCTYPE html>
<html lang="en">
<head>
<meta charset="utf-8">
<title>Orbit Lanternway – Business Cards</title>
<link rel="stylesheet" href="https://fonts.googleapis.com/css2?family=Alegreya+Sans:ital,wght@0,400;0,700;1,400&display=swap">
<style>
  :root {
    --bg: #e8e8ea;
    --navy: #12264a;
    --teal: #133f55;
    --stripe: #10304a;
    --ink: #eef2f6;
    --shadow: rgba(0, 0, 0, 0.22);
  }
  * { margin: 0; padding: 0; box-sizing: border-box; }
  html, body {
    width: 1200px;
    height: 740px;
    overflow: hidden;
    background: var(--bg);
  }
  .stage {
    position: relative;
    width: 1200px;
    height: 740px;
    font-family: "Alegreya Sans", sans-serif;
    color: var(--ink);
  }
  .card {
    position: absolute;
    top: 220px;
    width: 525px;
    height: 300px;
    overflow: hidden;
    background: var(--navy);
    box-shadow: 0 10px 24px var(--shadow);
  }
  .card--back { left: 50px; }
  .card--front { left: 625px; }

  /* bands */
  .band { position: absolute; left: 0; right: 0; background: var(--teal); }
  .card--back .band--top { top: 0; height: 48px; }
  .card--back .band--bottom { bottom: 0; height: 78px; }
  .card--back .stripe {
    position: absolute; left: 0; right: 0; bottom: 56px; height: 7px;
    background: var(--stripe);
  }
  .card--back .band--side {
    position: absolute; top: 48px; bottom: 78px; left: 0; width: 0;
  }
  .card--front .band--bottom { bottom: 0; height: 98px; }
  .card--front .band--side {
    position: absolute; top: 0; bottom: 0; left: 0; width: 40px;
    background: var(--teal);
  }

  /* brand lockup */
  .brand {
    position: absolute;
    left: 0; right: 0;
    display: flex;
    align-items: center;
    justify-content: center;
    gap: 14px;
  }
  .brand__mark {
    width: 34px; height: 34px;
    border-radius: 50%;
    background: var(--ink);
    flex: none;
  }
  .brand__text { text-align: left; }
  .brand__name {
    font-weight: 700;
    font-size: 27px;
    letter-spacing: 0.5px;
    line-height: 1.05;
  }
  .brand__tagline {
    font-style: italic;
    font-size: 15px;
    letter-spacing: 0.3px;
  }
  .card--back .brand { top: 62px; }
  .card--front .brand { top: 100px; }

  .services {
    position: absolute;
    top: 132px;
    left: 30px; right: 30px;
    text-align: center;
    font-size: 11.5px;
    line-height: 1.45;
  }
  .website {
    position: absolute;
    left: 0; right: 0;
    text-align: center;
    font-weight: 700;
    font-size: 20px;
    letter-spacing: 0.3px;
  }
  .card--back .website { bottom: 20px; }
  .card--front .website { bottom: 36px; font-size: 22px; }
</style>
</head>
<body>
<main class="stage">

  <section class="card card--back" aria-label="Business card, back">
    <div class="band band--top"></div>
    <div class="brand">
      <span class="brand__mark" aria-hidden="true"></span>
      <div class="brand__text">
        <div class="brand__name">Orbit Lanternway</div>
        <div class="brand__tagline">(Digital Business Consultancy)</div>
      </div>
    </div>
    <p class="services">
      Specialises in Digital Media Strategy, Digital Business Model Transformation,<br>
      Over-The-Top (OTT) Development, Web Business Development,<br>
      Digital Marketing, Web and App Product Development, Design and Innovation
    </p>
    <div class="stripe"></div>
    <div class="band band--bottom"></div>
    <p class="website">www.orbit-lanternway.example</p>
  </section>

  <section class="card card--front" aria-label="Business card, front">
    <div class="band--side"></div>
    <div class="band band--bottom"></div>
    <div class="brand">
      <span class="brand__mark" aria-hidden="true"></span>
      <div class="brand__text">
        <div class="brand__name">Orbit Lanternway</div>
        <div class="brand__tagline">(Digital Business Consultancy)</div>
      </div>
    </div>
    <p class="website">www.orbit-lanternway.example</p>
  </section>

</main>
</body>
</html>
```